Business Card Design with existing logo

AmberOwl provides inspirational leadership training and coaching for corporate executives. We focus on being challenging, humorous and compassionate, providing the right mix of support and push for individuals and teams to improve their knowledge and performance. The colour purple is essential to the design. We already have a logo we are very happy with - we are curious to see what can be done to come across in a professional, high standard way that sets us apart. Ideally the design should include the photo of Brigitte
Target Market(s)
HR/ Senior Management 500 - 1500 employees
Industry/Entity Type
Leadership
Contact Information for Business Card
AmberOwl Coaching Ltd
Inspirational leadership
Brigitte Holmqvist Dunmore
Leadership coach and trainer
Telephone: +44 1632 960 418
Mobile: +44 7700 900 562
e-mail: brigitte@amberowlmentoring.example
www.amberowlmentoring.example
Requirements
Must have
- The existing logo
Picture of Brigitte

```html
<!DOCTYPE html>
<html lang="en">
<head>
<meta charset="utf-8">
<title>AmberOwl Coaching – Business Card</title>
<link rel="stylesheet" href="https://fonts.googleapis.com/css2?family=Fira+Sans+Condensed:wght@400;500&display=swap">
<style>
  :root {
    --purple: #6c3aa6;
    --white: #ffffff;
    --ink: #3a3a3a;
    --stage: #e9e9ec;
    --photo-light: #d8d8d8;
    --photo-dark: #7c7c7c;
  }
  * { box-sizing: border-box; margin: 0; padding: 0; }
  html, body { width: 1200px; height: 848px; overflow: hidden; }
  body {
    background: var(--stage);
    font-family: "Fira Sans Condensed", "Arial Narrow", sans-serif;
    display: flex; align-items: center; justify-content: center; gap: 60px;
  }
  .card {
    position: relative; width: 525px; height: 300px; overflow: hidden;
    background: var(--white);
    box-shadow: 0 6px 18px rgba(0,0,0,.18);
  }
  .wordmark { font-size: 24px; font-weight: 500; color: var(--purple); line-height: 1; white-space: nowrap; }

  /* front */
  .front .wordmark { position: absolute; left: 26px; top: 28px; }
  .identity { position: absolute; left: 26px; top: 78px; }
  .person-name { font-size: 22px; font-weight: 500; color: var(--ink); white-space: nowrap; }
  .person-role { font-size: 16px; color: var(--purple); margin-top: 2px; }
  .band { position: absolute; left: 0; right: 0; top: 140px; height: 136px; background: var(--purple); }
  .contact { position: absolute; display: flex; align-items: center; gap: 8px; color: var(--white); font-size: 15px; white-space: nowrap; }
  .contact.phone { left: 26px; top: 166px; }
  .contact.mobile { left: 180px; top: 166px; }
  .contact.email { left: 26px; top: 204px; }
  .icon { width: 17px; height: 17px; border-radius: 4px; background: var(--white); display: flex; align-items: center; justify-content: center; flex: none; }
  .photo {
    position: absolute; right: 22px; top: 78px; width: 165px; height: 128px;
    border: 4px solid var(--white);
    background: linear-gradient(135deg, var(--photo-light), var(--photo-dark));
  }

  /* back */
  .back { background: var(--purple); }
  .back .stripe { position: absolute; left: 0; right: 0; top: 62px; height: 96px; background: var(--white); display: flex; align-items: center; padding-left: 46px; }
  .back .site { position: absolute; left: 60px; top: 190px; color: var(--white); font-size: 17px; }
</style>
</head>
<body>
  <section class="card front">
    <div class="wordmark">AmberOwl Coaching</div>
    <div class="identity">
      <div class="person-name">Brigitte Holmqvist Dunmore</div>
      <div class="person-role">Leadership coach and trainer</div>
    </div>
    <div class="band"></div>
    <div class="contact phone">
      <span class="icon"><svg width="11" height="11" viewBox="0 0 24 24"><path fill="#6c3aa6" d="M6.6 10.8a15 15 0 0 0 6.6 6.6l2.2-2.2a1 1 0 0 1 1-.25 11.4 11.4 0 0 0 3.6.6 1 1 0 0 1 1 1V20a1 1 0 0 1-1 1A17 17 0 0 1 3 4a1 1 0 0 1 1-1h3.5a1 1 0 0 1 1 1c0 1.25.2 2.45.6 3.6a1 1 0 0 1-.25 1z"/></svg></span>
      <span>+44 1632 960 418</span>
    </div>
    <div class="contact mobile">
      <span class="icon"><svg width="11" height="11" viewBox="0 0 24 24"><rect x="6" y="2" width="12" height="20" rx="2" fill="none" stroke="#6c3aa6" stroke-width="2.5"/><circle cx="12" cy="18" r="1.4" fill="#6c3aa6"/></svg></span>
      <span>+44 7700 900 562</span>
    </div>
    <div class="contact email">
      <span class="icon"><svg width="11" height="11" viewBox="0 0 24 24"><circle cx="12" cy="12" r="4" fill="none" stroke="#6c3aa6" stroke-width="2.5"/><path d="M16 8v5.5a2.5 2.5 0 0 0 5 0V12a9 9 0 1 0-3.5 7.1" fill="none" stroke="#6c3aa6" stroke-width="2.5"/></svg></span>
      <span>brigitte@amberowlmentoring.example</span>
    </div>
    <div class="photo" role="img" aria-label="Black and white portrait photo of Brigitte"></div>
  </section>

  <section class="card back">
    <div class="stripe">
      <div class="wordmark">AmberOwl Coaching</div>
    </div>
    <div class="site">www.amberowlmentoring.example</div>
  </section>
</body>
</html>
```